Business Card design for new private practice opening

I need a business card design for my new private practice with my new logo uploaded as a file
On the front the logo
On the back: maybe a small logo somewhere?
Priv. Doz. DDr. Corinna Vestaluk
Fachärztin für Allgemein- & Viszeralchirurgie
Address: xxx
Tel: xxx
Mobil:xxx
Webseite:xxx
Email:xxx

Contact Information for Business Card

See project description above for details

Requirements
Nice to have
• I would like the colors of the logo incorporated into the business card

```html
<!DOCTYPE html>
<html lang="de">
<head>
<meta charset="utf-8">
<title>Visitenkarte – Priv. Doz. DDr. Corinna Vestaluk</title>
<link rel="stylesheet" href="https://fonts.googleapis.com/css2?family=Mulish:wght@400;500;700;800&display=swap">
<style>
  :root {
    --bg: #eeeeee;
    --card: #ffffff;
    --teal: #5bb8b9;
    --teal-line: #4fa9aa;
    --ring: #8f8f8f;
    --ink: #666666;
    --ink-soft: #8a8a8a;
  }
  * { box-sizing: border-box; margin: 0; padding: 0; }
  html, body {
    width: 1200px; height: 800px; overflow: hidden;
    background: var(--bg);
    font-family: "Mulish", sans-serif;
  }
  .canvas { position: relative; width: 1200px; height: 800px; }
  .card {
    position: absolute;
    width: 520px; height: 300px;
    background: var(--card);
    box-shadow: 0 6px 18px rgba(0,0,0,0.08);
  }
  .card-front { left: 60px; top: 90px; }
  .card-back { left: 620px; top: 410px; }
  .rule {
    position: absolute; left: 0; right: 0; bottom: 42px;
    height: 3px; background: var(--teal-line);
  }
  .brand-mark {
    position: absolute; left: 50%; top: 46%;
    transform: translate(-50%, -50%);
    display: flex; align-items: center; gap: 14px;
    color: var(--teal);
    font-weight: 700; font-size: 26px; letter-spacing: 0.5px;
    white-space: nowrap;
  }
  .brand-dot {
    width: 46px; height: 46px; border-radius: 50%;
    border: 4px solid var(--ring);
  }
  .back-header {
    position: absolute; left: 34px; top: 40px;
    display: flex; align-items: center; gap: 18px;
  }
  .brand-small {
    display: flex; flex-direction: column; align-items: center; gap: 4px;
    color: var(--teal); font-weight: 700; font-size: 10px;
  }
  .brand-small .brand-dot { width: 44px; height: 44px; border-width: 3px; }
  .person-name {
    color: var(--ink); font-weight: 800; font-size: 21px; line-height: 1.2;
  }
  .person-title {
    color: var(--ink-soft); font-weight: 500; font-size: 14px; margin-top: 4px;
  }
  .contact-list {
    position: absolute; left: 138px; top: 128px;
    list-style: none;
  }
  .contact-item {
    display: flex; align-items: center; gap: 10px;
    color: var(--ink-soft); font-size: 13px; line-height: 23px;
  }
  .contact-item svg { width: 14px; height: 14px; fill: var(--ink); flex: none; }
</style>
</head>
<body>
<div class="canvas">
  <section class="card card-front" aria-label="Vorderseite">
    <div class="brand-mark"><span class="brand-dot"></span>Praxis Vestaluk</div>
    <div class="rule"></div>
  </section>

  <section class="card card-back" aria-label="Rückseite">
    <header class="back-header">
      <div class="brand-small"><span class="brand-dot"></span>Praxis Vestaluk</div>
      <div>
        <h1 class="person-name">Priv. Doz. DDr. Corinna Vestaluk</h1>
        <p class="person-title">Fachärztin für Allgemein- &amp; Viszeralchirurgie</p>
      </div>
    </header>
    <ul class="contact-list">
      <li class="contact-item">
        <svg viewBox="0 0 24 24"><path d="M12 2a7 7 0 0 0-7 7c0 5 7 13 7 13s7-8 7-13a7 7 0 0 0-7-7zm0 9.5A2.5 2.5 0 1 1 12 6.5a2.5 2.5 0 0 1 0 5z"/></svg>
        Adress: xxx
      </li>
      <li class="contact-item">
        <svg viewBox="0 0 24 24"><path d="M6.6 10.8a15 15 0 0 0 6.6 6.6l2.2-2.2c.3-.3.7-.4 1-.2 1.1.4 2.3.6 3.6.6.6 0 1 .4 1 1V20c0 .6-.4 1-1 1A17 17 0 0 1 3 4c0-.6.4-1 1-1h3.5c.6 0 1 .4 1 1 0 1.3.2 2.5.6 3.6.1.3 0 .7-.2 1z"/></svg>
        Tel: xxx
      </li>
      <li class="contact-item">
        <svg viewBox="0 0 24 24"><path d="M7 1h10a2 2 0 0 1 2 2v18a2 2 0 0 1-2 2H7a2 2 0 0 1-2-2V3a2 2 0 0 1 2-2zm0 3v14h10V4zm5 15.5a1 1 0 1 0 0 2 1 1 0 0 0 0-2z"/></svg>
        Mobil: xxx
      </li>
      <li class="contact-item">
        <svg viewBox="0 0 24 24"><path d="M12 2a10 10 0 1 0 0 20 10 10 0 0 0 0-20zm6.9 6h-2.9a15 15 0 0 0-1.4-3.6A8 8 0 0 1 18.9 8zM12 4c.8 1.2 1.5 2.5 1.9 4h-3.8c.4-1.5 1.1-2.8 1.9-4zM4.3 14a8 8 0 0 1 0-4h3.4a16 16 0 0 0 0 4zm.8 2h2.9c.3 1.3.8 2.5 1.4 3.6A8 8 0 0 1 5.1 16zM8 8H5.1a8 8 0 0 1 4.3-3.6C8.8 5.5 8.3 6.7 8 8zm4 12c-.8-1.2-1.5-2.5-1.9-4h3.8c-.4 1.5-1.1 2.8-1.9 4zm2.3-6H9.7a14 14 0 0 1 0-4h4.6a14 14 0 0 1 0 4zm.3 5.6c.6-1.1 1.1-2.3 1.4-3.6h2.9a8 8 0 0 1-4.3 3.6zm1.7-5.6a16 16 0 0 0 0-4h3.4a8 8 0 0 1 0 4z"/></svg>
        Webseite: xxx
      </li>
      <li class="contact-item">
        <svg viewBox="0 0 24 24"><path d="M2 5h20v14H2zm2 2v.5l8 5 8-5V7zm0 2.9V17h16V9.9l-8 5z"/></svg>
        Email: xxx
      </li>
    </ul>
    <div class="rule"></div>
  </section>
</div>
</body>
</html>
```